Letter Head, for use on daily correspondence with other companies

Hi

I want a professional Letter head, That my company can use to corresponded with other companies we do business with on a daily basis.

I want this done as soon as possible as this is peak session for us.

I have attached the company logo so please be creative and professional.
Kind regards

Marcus

Target Market(s)

All Audience searching for tickets, people in the entertainment world

Industry/Entity Type

Entertainment Industry

Font styles to use
Serif
Sans Serif
Decorative
Script

Requirements
Must have
• Very professional image.
• I will know want i want when i see it
• so please do your utmost in your professional standards
• Address of the company 24 hollin lane, telephone number 0207 562 3198
• Vat number: 487 2915 06.
• This letter head my be able to acomodate usage for directors & CEO as well as managers and employess
Nice to have
• A great professional image
Should not have
• Be creative please

```html
<!DOCTYPE html>
<html lang="en">
<head>
<meta charset="utf-8">
<title>Brightseat Tickets Letterhead</title>
<link rel="stylesheet" href="https://fonts.googleapis.com/css2?family=Montserrat:wght@400;700&family=Courier+Prime:wght@700&display=swap">
<style>
  :root {
    --backdrop: #ddd0b8;
    --paper: #ffffff;
    --brand-red: #c92112;
    --ink: #555555;
    --address-ink: #1d1d1d;
    --seal-blue: #8aa3d6;
    --signature-ink: #3a3a3a;
  }
  * { margin: 0; padding: 0; box-sizing: border-box; }
  html, body {
    width: 1200px;
    height: 900px;
    overflow: hidden;
    background: var(--backdrop);
  }
  .letterhead {
    position: absolute;
    left: 296px;
    top: 20px;
    width: 608px;
    height: 860px;
    background: var(--paper);
    overflow: hidden;
    box-shadow: 0 6px 24px rgba(0, 0, 0, 0.12);
  }
  .brand-block {
    position: absolute;
    left: 24px;
    top: 30px;
    width: 118px;
    height: 96px;
    background: var(--brand-red);
    display: flex;
    align-items: center;
    justify-content: center;
  }
  .brand-name {
    font-family: "Montserrat", sans-serif;
    font-weight: 700;
    font-size: 15px;
    color: var(--paper);
    text-align: center;
    line-height: 1.15;
  }
  .letter-body {
    position: absolute;
    left: 120px;
    top: 250px;
    width: 440px;
    font-family: "Montserrat", sans-serif;
    font-size: 9px;
    line-height: 1.7;
    color: var(--ink);
  }
  .letter-body p { margin-bottom: 15px; }
  .letter-body p:last-child { margin-bottom: 0; }
  .corner-sweep {
    position: absolute;
    right: 0;
    bottom: 0;
    width: 608px;
    height: 860px;
  }
  .sign-off {
    position: absolute;
    left: 432px;
    top: 604px;
    font-family: "Montserrat", sans-serif;
    font-size: 9px;
    color: var(--ink);
  }
  .notary-seal {
    position: absolute;
    left: 412px;
    top: 622px;
    width: 84px;
    height: 84px;
    border: 2px solid var(--seal-blue);
    border-radius: 50%;
  }
  .signature {
    position: absolute;
    left: 426px;
    top: 643px;
    width: 56px;
    height: 42px;
    border-radius: 6px;
    background: linear-gradient(135deg, rgba(58,58,58,0.35), rgba(58,58,58,0.12));
  }
  .company-details {
    position: absolute;
    left: 26px;
    bottom: 22px;
    font-family: "Courier Prime", monospace;
    font-weight: 700;
    font-size: 13px;
    line-height: 1.05;
    color: var(--address-ink);
  }
</style>
</head>
<body>
  <main class="letterhead">
    <svg class="corner-sweep" viewBox="0 0 608 860" aria-hidden="true">
      <path d="M608 455 C 560 620, 420 780, 250 860 L 608 860 Z" fill="var(--brand-red)"/>
    </svg>

    <header class="brand-block">
      <span class="brand-name">Brightseat<br>Tickets</span>
    </header>

    <section class="letter-body">
      <p>Lorem ipsum dolor sit amet, consectetur adipiscing elit. Donec orci purus, luctus vitae dignissim eu, iaculis sed purus. Vivamus faucibus, ipsum nec aliquet viverra, leo mauris condimentum ligula, sit amet sagittis enim ligula quis arcu. Nam egestas tortor id nisi porttitor mattis. In tortor ante, ultricies in suscipit a, tempus non massa. Vivamus et auctor mi. Fusce vel massa nulla. Phasellus nec eros mauris, et scelerisque orci.</p>
      <p>Donec malesuada orci vitae nulla accumsan porta a id massa. Quisque accumsan iaculis magna sit amet fringilla. Maecenas consequat, magna eget tincidunt semper, odio nibh rutrum mi, id feugiat ante nisi eu risus. Vestibulum nunc orci, rhoncus a placerat in, ultricies in mi. Cras mattis varius eros, vel fringilla nisi suscipit eget. Quisque scelerisque sagittis nulla at porttitor.</p>
      <p>Sed id augue vitae urna euismod commodo aliquet a quam. Pellentesque arcu velit, cursus et malesuada ut, consequat et diam. Nullam erat sem, rhoncus id ullamcorper vitae, rhoncus et arcu. In ultricies ultricies nulla, ut rutrum nisi iaculis at. Donec eu magna a metus ornare faucibus. Fusce aliquet faucibus ultricies. Morbi semper, est id tincidunt gravida, sem arcu adipiscing lacus, ac bibendum nulla leo eu purus. Quisque nec diam sed risus consectetur accumsan quis quis nibh. Vestibulum id purus lorem.</p>
    </section>

    <p class="sign-off">Sincerely,</p>
    <div class="notary-seal" aria-hidden="true"></div>
    <div class="signature" role="img" aria-label="Handwritten signature"></div>

    <footer class="company-details">
      <div>24 Hollin Lane</div>
      <div>Tel: 0207 562 3198</div>
      <div>Vat: 487 2915 06</div>
    </footer>
  </main>
</body>
</html>
```